Fenwick Quarter Summer Party Invitation

We need an invitation to be designed for our annual summer party for Fenwick Quarter in Chelsea, London. The area has a relaxed family atmosphere but is on the edge of the bustle of Chelsea. The committee has specified the following:

TO INCLUDE THE FOLLOWING INFORMATION - will it be the same two sided format as last year? Maybe the reverse can use your pale blue and your London skyline "logo"

Should the following, highlighted in blue, be very bold on the front of the invite? With the Harlow & Pike sales and lettings logo.
SUMMER PARTY 2016
Fenwick Quarter Chelsea is holding a Summer Party to celebrate the Duke's 90th Birthday

Date: Saturday 18th June 2016
Time: 2.00pm to 5.00pm
Place: Brimble Lane South (the pedestrianised section off Ockenden Street) MAP?

Open to all residents of Fenwick Quarter and admittance is by invitation only.
Please keep this invitation safe and bring it with you on the day

Then more detail on the rear:

Fenwick Quarter Chelsea
Formerly known as Dunmere Residents' Association of Fenwick Quarter

Email: dunmerera@postbox-mail.test
Website: dunmerera-example.co.uk
OUR TYPEFACE IS ARIAL. The rest can be in any typeface but Arial is our "logo"

Dress code: red white and blue (or black ) as simple or elaborate as you like Live Music Children's entertainment and activities Food Drinks Tea and cakes

SPONSORS:
Harlow & Pike. Ensuring this is prominent as the main sponsor Kestrel Arms
412 Blues club etc etc
Larkfield Yard Studios
List to follow.............

Space needs to be left on the rear for sponsors details to be added. They would like something with an almost retro, traditional British feel.
Our Harlow & Pike logo attached and branding.

Also a flyer that association seemed to like.

I would suggest postcard (A6 sized) or maybe A5 at the biggest

Target Market(s)

Local Residents

Colors
ec1f27
ffffff
0355a3

Requirements
Must have
• Information on the description

```html
<!DOCTYPE html>
<html lang="en">
<head>
<meta charset="utf-8">
<title>Fenwick Quarter Summer Party Invitation</title>
<link rel="stylesheet" href="https://fonts.googleapis.com/css2?family=Lobster&family=Roboto+Condensed:wght@300;400;700&display=swap">
<style>
  :root {
    --page: #ffffff;
    --teal: #5fb6bd;
    --teal-deep: #3f9aa6;
    --teal-pale: #a9dcdc;
    --cream: #fdf5cf;
    --cream-light: #fffbe8;
    --royal: #1f4f9e;
    --royal-dark: #173a7a;
    --sky: #2b9bd4;
    --navy-text: #2f3d6e;
    --map-grey: #e6e3dc;
  }
  * { margin: 0; padding: 0; box-sizing: border-box; }
  html, body { width: 1200px; height: 1000px; overflow: hidden; background: var(--page); }
  body { position: relative; font-family: "Roboto Condensed", Arial, sans-serif; }

  .card { position: absolute; top: 73px; height: 842px; overflow: hidden; }
  .card--front { left: 0; width: 597px; }
  .card--back { left: 604px; width: 596px; }

  .bunting-strip {
    position: absolute; top: 0; height: 100%;
    background: linear-gradient(180deg, var(--teal-pale), var(--teal) 40%, var(--teal-deep) 70%, var(--teal));
  }
  .bunting-top {
    position: absolute; left: 0; top: 0; width: 100%; height: 125px;
    background: linear-gradient(180deg, var(--teal-deep), var(--teal) 60%, var(--teal-pale));
  }
  .paper {
    position: absolute;
    background: radial-gradient(ellipse at 50% 45%, var(--cream-light), var(--cream) 70%);
  }
  .skyline {
    position: absolute; left: 81px; top: 88px; width: 443px; height: 38px;
    background: linear-gradient(180deg, var(--cream), var(--cream-light));
    border-radius: 3px 3px 0 0;
  }

  .centered { position: absolute; width: 100%; text-align: center; left: 0; }

  .title-script {
    font-family: "Lobster", cursive; color: var(--royal);
    text-shadow: 2px 3px 0 var(--royal-dark), 4px 6px 6px rgba(0,0,0,.25);
    line-height: 1;
  }
  .title-summer { top: 54px; font-size: 108px; }
  .title-party { top: 122px; font-size: 100px; }
  .title-year { top: 234px; font-size: 48px; }

  .rule { position: absolute; height: 2px; background: var(--royal); }

  .tagline {
    font-family: "Lobster", cursive; color: var(--sky);
    font-size: 18px; line-height: 21px;
  }

  .details { color: var(--navy-text); font-size: 22px; line-height: 28px; font-weight: 300; }
  .details strong { font-weight: 700; color: var(--royal-dark); }
  .details .note { font-size: 15px; line-height: 20px; }

  .map {
    position: absolute; left: 176px; top: 504px; width: 241px; height: 183px;
    background: var(--map-grey);
  }

  .notice { color: var(--sky); font-size: 17px; line-height: 20px; font-weight: 300; }

  .back-title { font-family: "Lobster", cursive; color: var(--royal); font-size: 41px; }
  .contact { color: var(--navy-text); font-size: 21px; line-height: 28px; font-weight: 300; }
  .contact strong { font-weight: 700; color: var(--royal-dark); font-size: 22px; }
  .dress { color: var(--navy-text); font-size: 18px; line-height: 21px; font-weight: 300; }
  .features { color: var(--sky); font-size: 14.5px; line-height: 17px; font-weight: 300; letter-spacing: 1px; }
  .sponsors-label { color: var(--navy-text); font-size: 17px; font-weight: 300; }
  .sponsor-main { color: var(--royal-dark); font-size: 30px; font-weight: 700; letter-spacing: .5px; }
  .sponsor-list { color: var(--navy-text); font-size: 14px; line-height: 20px; }
</style>
</head>
<body>

<section class="card card--front">
  <div class="bunting-strip" style="left:0;width:73px" role="img" aria-label="Red, white and blue bunting flags hanging down the left edge"></div>
  <div class="bunting-strip" style="left:523px;width:74px" role="img" aria-label="Red, white and blue bunting flags hanging down the right edge"></div>
  <div class="paper" style="left:73px;top:0;width:450px;height:100%"></div>

  <h1>
    <span class="centered title-script title-summer">Summer</span>
    <span class="centered title-script title-party">Party</span>
    <span class="centered title-script title-year">2016</span>
  </h1>

  <div class="rule" style="left:118px;top:309px;width:360px"></div>
  <p class="centered tagline" style="top:316px">Fenwick Quarter Chelsea is holding a Summer<br>Party to celebrate the Duke's 90th Birthday</p>
  <div class="rule" style="left:118px;top:365px;width:360px"></div>

  <div class="centered details" style="top:390px">
    <p>Date: <strong>Saturday 18th June 2016</strong></p>
    <p>Time: <strong>2.00pm to 5.00pm</strong></p>
    <p>Place: <strong>Brimble Lane South</strong></p>
    <p class="note">(the pedestrianised section of Ockenden Street)</p>
  </div>

  <div class="map" role="img" aria-label="Street map showing Brimble Lane South off Ockenden Street"></div>

  <p class="centered notice" style="top:709px">Open to all residents of Fenwick Quarter and<br>admittance is by invitation only.<br>Please keep this invitation safe and bring<br>it with you on the day.</p>
</section>

<section class="card card--back">
  <div class="bunting-top" role="img" aria-label="Bunting flags strung along the top edge"></div>
  <div class="bunting-strip" style="left:0;width:81px" role="img" aria-label="Bunting flags down the left edge"></div>
  <div class="bunting-strip" style="left:524px;width:72px" role="img" aria-label="Bunting flags down the right edge"></div>
  <div class="paper" style="left:81px;top:124px;width:443px;height:718px"></div>
  <div class="skyline" role="img" aria-label="London skyline silhouette"></div>

  <h2 class="centered back-title" style="top:178px">Fenwick Quarter Chelsea</h2>

  <div class="rule" style="left:148px;top:259px;width:302px;background:var(--sky)"></div>
  <p class="centered tagline" style="top:268px;color:var(--royal)">Formerly known as Dunmere<br>Residents' Association of Fenwick Quarter</p>
  <div class="rule" style="left:148px;top:314px;width:302px;background:var(--sky)"></div>

  <div class="centered contact" style="top:346px">
    <p>Email:</p>
    <p><strong>dunmerera@postbox-mail.test</strong></p>
    <p>Website:</p>
    <p><strong>dunmerera-example.co.uk</strong></p>
  </div>

  <p class="centered dress" style="top:476px"><em>Dress code:</em> red white and blue (or black )<br>as simple or elaborate as you like</p>

  <p class="centered features" style="top:540px">Live Music • Children's entertainment<br>and activities • Food Drinks • Tea and cakes</p>

  <p class="centered sponsors-label" style="top:605px">SPONSORS</p>
  <p class="centered sponsor-main" style="top:632px">Harlow &amp; Pike</p>
  <p class="centered sponsor-list" style="top:689px">412 Blues club<br>Larkfield Yard Studios</p>
</section>

</body>
</html>
```